Vordaline - Fitness Coach. Needs a Business Card Design that I can also use for other advertising

Established 2012, I have finished the KTRB National Certificate in Fitness & Personal Training. Harlow Cross First Aid Certificate. I have the Auckland 800m track records for MW45. I also came 1st at the 2012 Pellamar Games in 800 & 1500m. I am passionate about health & fitness and would like to help people reach their health & fitness goals. I also take health & fitness weekends. Main interests - Running, Weight Training, Yoga & Aqua Jogging. I like strength/power, but am femine.

Target Market(s)

Male or Female 18 and over that wants to improve their health & fitness

Industry/Entity Type

Advertising

Requirements
Must have
• my name: Rosalind K Tarbury contact details: ros@quillsend.co.nz mobile - 021 583917 URL name: facebook.com/rosalindKtarbury - VordaLine
Photo of Me

```html
<!DOCTYPE html>
<html lang="en">
<head>
<meta charset="utf-8">
<title>Vordaline – Fitness Coach Business Card</title>
<link rel="stylesheet" href="https://fonts.googleapis.com/css2?family=Anton&family=Roboto+Condensed:wght@700;800;900&display=swap">
<style>
  :root {
    --backdrop: #2a2a2c;
    --blue-deep: #0b4596;
    --blue-mid: #1170b8;
    --blue-light: #1a96d4;
    --yellow: #ffdd00;
    --gold: #e9b400;
    --orange: #f26a1b;
    --pink: #e6156b;
    --white: #ffffff;
    --ink: #1b1b1b;
    --rule: rgba(160, 210, 245, 0.55);
  }
  * { box-sizing: border-box; margin: 0; padding: 0; }
  html, body {
    width: 1200px; height: 900px; overflow: hidden;
    background: var(--backdrop);
  }
  .canvas { position: relative; width: 1200px; height: 900px; }

  .card {
    position: absolute; top: 300px;
    width: 540px; height: 300px;
    border-radius: 14px; overflow: hidden;
    box-shadow: 0 4px 10px rgba(0,0,0,0.45);
  }
  .card--front {
    left: 45px;
    background: linear-gradient(100deg, var(--blue-deep) 0%, var(--blue-mid) 45%, var(--blue-light) 75%);
    font-family: "Roboto Condensed", "Arial Narrow", sans-serif;
  }
  .card--back {
    left: 615px;
    background: var(--yellow);
    display: flex; align-items: center; justify-content: center;
  }

  .front-art { position: absolute; inset: 0; width: 540px; height: 300px; }

  .brand {
    position: absolute; left: 22px; top: 40px;
    font-family: "Roboto Condensed", "Arial Narrow", sans-serif;
    font-weight: 900; font-size: 50px; line-height: 1;
    color: var(--yellow); letter-spacing: -0.5px;
  }
  .coach-name {
    position: absolute; left: 22px; top: 118px;
    font-weight: 800; font-size: 24px; color: var(--yellow);
  }
  .coach-role {
    position: absolute; left: 22px; top: 145px;
    font-weight: 800; font-size: 20px; color: var(--white);
  }
  .coach-tagline {
    position: absolute; left: 22px; top: 170px;
    font-weight: 700; font-size: 11.5px; color: var(--white);
  }

  .contact-list {
    position: absolute; left: 0; top: 200px; width: 228px;
    list-style: none;
    border-top: 1px solid var(--rule);
  }
  .contact-item {
    display: flex; align-items: center; gap: 10px;
    height: 22px; padding-left: 24px;
    border-bottom: 1px solid var(--rule);
    background: rgba(255,255,255,0.05);
    font-weight: 700; font-size: 11.5px; color: var(--white);
  }
  .contact-icon { width: 14px; height: 14px; flex: none; }

  .services {
    list-style: none; text-align: center;
    font-family: "Anton", "Impact", sans-serif;
    font-size: 40px; line-height: 52px; color: var(--ink);
    letter-spacing: 0.3px;
  }
</style>
</head>
<body>
<main class="canvas">

  <section class="card card--front" aria-label="Business card front">
    <svg class="front-art" viewBox="0 0 540 300" aria-hidden="false">
      <defs>
        <linearGradient id="swoosh-red" x1="0" y1="1" x2="1" y2="0">
          <stop offset="0" stop-color="#f58220"/>
          <stop offset="0.5" stop-color="var(--orange)"/>
          <stop offset="1" stop-color="var(--pink)"/>
        </linearGradient>
        <linearGradient id="swoosh-gold" x1="0" y1="1" x2="1" y2="0">
          <stop offset="0" stop-color="#f7a21b"/>
          <stop offset="0.45" stop-color="var(--yellow)"/>
          <stop offset="1" stop-color="var(--gold)"/>
        </linearGradient>
        <linearGradient id="photo-tone" x1="0" y1="0" x2="0" y2="1">
          <stop offset="0" stop-color="#3f6a2a"/>
          <stop offset="0.6" stop-color="#2f5a22"/>
          <stop offset="1" stop-color="#5e8f36"/>
        </linearGradient>
      </defs>
      <path class="swoosh swoosh--red" d="M214,300 C222,160 276,45 350,0 L540,0 L540,300 Z" fill="url(#swoosh-red)"/>
      <path class="swoosh-gap" d="M227,300 C236,168 288,58 372,14 L540,12 L540,300 Z" fill="#ffffff"/>
      <path class="swoosh swoosh--gold" d="M231,300 C240,172 292,62 378,18 L540,16 L540,300 Z" fill="url(#swoosh-gold)"/>
      <path class="swoosh-gap" d="M244,300 C254,185 305,88 392,44 L540,42 L540,300 Z" fill="#ffffff"/>
      <path class="swoosh swoosh--blue" d="M247,300 C257,188 308,92 396,48 L540,46 L540,300 Z" fill="var(--blue-mid)"/>
      <path class="coach-photo" role="img" aria-label="Photo of the coach jumping in fitness gear in front of a green hedge"
            d="M249,300 C259,192 310,96 398,58 L540,60 L540,300 Z" fill="url(#photo-tone)"/>
    </svg>

    <div class="brand">VORDALINE</div>
    <div class="coach-name">Rosalind K. Tarbury</div>
    <div class="coach-role">fitness coach</div>
    <div class="coach-tagline">meeting your health &amp; fitness goals</div>

    <ul class="contact-list">
      <li class="contact-item">
        <svg class="contact-icon" viewBox="0 0 14 14" aria-hidden="true">
          <rect x="1" y="3" width="12" height="8.5" fill="var(--yellow)"/>
          <path d="M1,3 L7,8 L13,3" fill="none" stroke="var(--blue-deep)" stroke-width="1"/>
        </svg>
        <span>ros@quillsend.co.nz</span>
      </li>
      <li class="contact-item">
        <svg class="contact-icon" viewBox="0 0 14 14" aria-hidden="true">
          <rect x="4" y="1" width="6.5" height="12" rx="1" fill="none" stroke="var(--yellow)" stroke-width="1.4"/>
          <circle cx="7.25" cy="11" r="0.8" fill="var(--yellow)"/>
        </svg>
        <span>021 583 917</span>
      </li>
      <li class="contact-item">
        <svg class="contact-icon" viewBox="0 0 14 14" aria-hidden="true">
          <rect x="1.5" y="1.5" width="11" height="11" fill="var(--yellow)"/>
        </svg>
        <span>rosalindktarbury</span>
      </li>
    </ul>
  </section>

  <section class="card card--back" aria-label="Business card back">
    <ul class="services">
      <li>RUNNING</li>
      <li>WEIGHT TRAINING</li>
      <li>YOGA</li>
      <li>AQUA JOGGING</li>
    </ul>
  </section>

</main>
</body>
</html>
```